Flyer for spiritual retreat (yoga, meditation, reiki, raw food)

I would like a flyer to promote my upcoming retreat and a matching Facebook banner.

The name of the retreat is "Wavecrest Of Calm" and the tagline is "retreat into you"

The activities in the retreat include daily meditation, ecstatic dance, spiritual development workshops on intuition, energy healing etc and a reiki session is included.

I would like a flyer designed to promote this, something that is editable as I will be running this multiple times and will need to adjust the flyer to add the dates etc each time.

edit: add that here will be fully catered raw food and juices, and that the retreat price includes all accomodation, meals and workshops.

Please contact me if you need further info. Please also visit my website www.marithovland.com and www.facebook.com/tolvanahaven to see my current events and promotions.

Thank you,

Marit

Reason: Hi all, thank you all for your submissions. Apologies as I am traveling and do not have much access to internet and will review your submissions and provide feedback as soon as possible. Kind regards, Marit.

Target Market(s)

People who like meditation, yoga, fans of rowan mabry and jasper vinek, those interested in personal and spiritual development.

Industry/Entity Type

Health And Wellness

Requirements
Must have
• Please put the included reiki session as as added bonus. Something like "BONUS 30 minute reiki healing session" in a little star/banner/something that stands out.
• Please emphasise the "light" part of Wavecrest as I am going for a play on words between in the light and enlightenment.
• Please include placeholder text for place, location, time
• Placeholder for price
• My name (see attached file - can change colour to suit) and website (www.marithovland.com)
Nice to have
• I prefer rounded designs, curves rather than block designs.
Should not have
• Tolvana Haven logo

```html
<!DOCTYPE html>
<html lang="en">
<head>
<meta charset="utf-8">
<title>Wavecrest Of Calm – Retreat Flyer</title>
<link rel="stylesheet" href="https://fonts.googleapis.com/css2?family=Anton&family=Roboto+Condensed:ital,wght@0,700;1,700;1,900&family=Roboto:ital,wght@1,400&family=Kaushan+Script&display=swap">
<style>
  :root {
    --green: #5aa23a;
    --green-dark: #3f7f27;
    --green-deep: #2f6a1c;
    --green-light: #6cb548;
    --ink: #161616;
    --red: #e0201c;
    --paper: #f4f4f6;
    --white: #ffffff;
    --stage: #e6e6e6;
  }
  html, body {
    margin: 0;
    width: 1200px;
    height: 1200px;
    overflow: hidden;
    background: var(--stage);
  }
  .flyer {
    position: absolute;
    left: 210px;
    top: 50px;
    width: 780px;
    height: 1100px;
    box-shadow: 0 6px 24px rgba(0,0,0,.25);
  }
  .fill-green { fill: var(--green); }
  .fill-green-dark { fill: var(--green-dark); }
  .fill-green-light { fill: var(--green-light); }
  .fill-ink { fill: var(--ink); }
  .fill-white { fill: var(--white); }
  .fill-paper { fill: var(--paper); }
  .brand-name { font-family: "Roboto Condensed", sans-serif; font-weight: 700; font-size: 34px; fill: var(--white); }
  .title { font-family: "Roboto Condensed", sans-serif; font-style: italic; font-weight: 700; font-size: 54px; fill: var(--green); }
  .title-light { font-weight: 900; fill: var(--green-deep); }
  .tagline { font-family: "Roboto", sans-serif; font-style: italic; font-size: 29px; fill: #333; letter-spacing: 3px; }
  .badge-bonus { font-family: "Roboto Condensed", sans-serif; font-style: italic; font-weight: 700; font-size: 48px; fill: var(--red); }
  .badge-minutes { font-family: "Anton", sans-serif; font-size: 40px; fill: var(--green); }
  .badge-reiki { font-family: "Roboto Condensed", sans-serif; font-style: italic; font-weight: 700; font-size: 30px; fill: var(--white); }
  .badge-session { font-family: "Roboto Condensed", sans-serif; font-style: italic; font-weight: 700; font-size: 48px; fill: var(--ink); }
  .date-day, .date-year { font-family: "Anton", sans-serif; font-size: 46px; fill: var(--green); }
  .date-month { font-family: "Anton", sans-serif; font-size: 27px; fill: var(--green); }
  .headline { font-family: "Anton", sans-serif; font-size: 48px; fill: var(--ink); }
  .offer { font-family: "Kaushan Script", cursive; font-size: 48px; fill: var(--red); }
  .address { font-family: "Roboto Condensed", sans-serif; font-weight: 700; font-size: 20px; fill: var(--white); }
  .details { font-family: "Roboto Condensed", sans-serif; font-weight: 700; font-size: 20px; fill: var(--green-light); }
  .website { font-family: "Anton", sans-serif; font-size: 31px; fill: var(--white); letter-spacing: .5px; }
  .cta { font-family: "Anton", sans-serif; font-size: 25px; fill: var(--ink); }
</style>
</head>
<body>
<svg class="flyer" viewBox="0 0 780 1100" xmlns="http://www.w3.org/2000/svg">
  <defs>
    <radialGradient id="photo-glow" cx="50%" cy="45%" r="60%">
      <stop offset="0" stop-color="#ffffff"/>
      <stop offset="1" stop-color="#eceef2"/>
    </radialGradient>
    <linearGradient id="thumb-beach" x1="0" y1="0" x2="0" y2="1">
      <stop offset="0" stop-color="#7fb6dc"/><stop offset="1" stop-color="#d9c7a6"/>
    </linearGradient>
    <linearGradient id="thumb-studio" x1="0" y1="0" x2="0" y2="1">
      <stop offset="0" stop-color="#dfe6ee"/><stop offset="1" stop-color="#c9a98a"/>
    </linearGradient>
    <linearGradient id="thumb-shore" x1="0" y1="0" x2="0" y2="1">
      <stop offset="0" stop-color="#9cc6e6"/><stop offset="1" stop-color="#d6cdb8"/>
    </linearGradient>
    <clipPath id="clip-t1"><circle cx="378" cy="711" r="58"/></clipPath>
    <clipPath id="clip-t2"><circle cx="531" cy="680" r="58"/></clipPath>
    <clipPath id="clip-t3"><circle cx="684" cy="642" r="58"/></clipPath>
  </defs>

  <!-- page -->
  <rect class="fill-paper" width="780" height="1100"/>

  <!-- hero photo area -->
  <rect x="20" y="120" width="420" height="600" fill="url(#photo-glow)" role="img" aria-label="Photo of a woman meditating cross-legged with arms raised in prayer pose"/>

  <!-- brand tab -->
  <g class="brand">
    <polygon class="fill-green" points="0,0 285,0 320,110 0,142"/>
    <text class="brand-name" x="28" y="80">Marit Hovland</text>
  </g>

  <!-- title -->
  <text class="title" x="762" y="162" text-anchor="end">Wave<tspan class="title-light">crest</tspan> Of Calm</text>
  <text class="tagline" x="718" y="205" text-anchor="end">RETREAT INTO YOU</text>

  <!-- bonus badge -->
  <g class="bonus-badge">
    <circle cx="598" cy="407" r="148" class="fill-white"/>
    <circle cx="598" cy="407" r="143" fill="none" stroke="var(--green)" stroke-width="9"/>
    <text class="badge-bonus" x="598" y="333" text-anchor="middle">BONUS</text>
    <text class="badge-minutes" x="598" y="380" text-anchor="middle">30 MINUTES</text>
    <polygon class="fill-ink" points="430,403 756,403 756,466 430,472"/>
    <text class="badge-reiki" x="595" y="446" text-anchor="middle">REIKI HEALING</text>
    <text class="badge-session" x="596" y="523" text-anchor="middle">SESSION</text>
  </g>

  <!-- footer bands -->
  <polygon class="fill-green" points="0,748 780,610 780,1100 0,1100"/>
  <polygon class="fill-green-light" points="0,748 300,700 360,800 0,812"/>
  <polygon class="fill-green-dark" points="300,800 380,790 560,1100 470,1100"/>
  <polygon class="fill-ink" points="0,812 300,800 470,1100 0,1100"/>

  <!-- gallery thumbnails -->
  <g class="gallery">
    <circle cx="378" cy="711" r="66" class="fill-white"/>
    <rect x="320" y="653" width="116" height="116" fill="url(#thumb-beach)" clip-path="url(#clip-t1)" role="img" aria-label="Photo of two women meditating on a beach"/>
    <circle cx="531" cy="680" r="66" class="fill-white"/>
    <rect x="473" y="622" width="116" height="116" fill="url(#thumb-studio)" clip-path="url(#clip-t2)" role="img" aria-label="Photo of a yoga class stretching in a studio"/>
    <circle cx="684" cy="642" r="66" class="fill-white"/>
    <rect x="626" y="584" width="116" height="116" fill="url(#thumb-shore)" clip-path="url(#clip-t3)" role="img" aria-label="Photo of a group doing tree pose by the sea"/>
  </g>

  <!-- date -->
  <g class="date-badge">
    <circle cx="153" cy="858" r="92" class="fill-white"/>
    <text class="date-day" x="153" y="831" text-anchor="middle">30</text>
    <text class="date-month" x="153" y="866" text-anchor="middle">DECEMBER</text>
    <text class="date-year" x="153" y="915" text-anchor="middle">2016</text>
  </g>

  <!-- headline -->
  <text class="headline" x="744" y="818" text-anchor="end">GET HEALTHY</text>
  <text class="headline" x="744" y="870" text-anchor="end">LIFE TODAY</text>

  <!-- offer -->
  <g class="offer-mark">
    <ellipse cx="605" cy="962" rx="148" ry="48" fill="none" stroke="var(--white)" stroke-width="6" transform="rotate(-6 605 962)"/>
    <text class="offer" x="605" y="978" text-anchor="middle" transform="rotate(-6 605 962)">50% save</text>
  </g>
  <text class="cta" x="612" y="1062" text-anchor="middle">COME AND JOIN US!</text>

  <!-- contact -->
  <text class="address" x="22" y="972">Unit 4, 27-31 Fernbrook Lane</text>
  <text class="address" x="22" y="997">Fernbrook VIC 3290</text>
  <text class="details" x="22" y="1022">Time: 9AM – 5PM  ·  Price: $000</text>
  <text class="website" x="22" y="1068">WWW.MARITHOVLAND.COM</text>
</svg>
</body>
</html>
```